A Gallery type Web design

We are developing a Wordpress based website for a client that does design construction projects. E.g. Pools, Lobbies, Toilets, etc. The website will mainly be to showcase their past projects and the collections they have.
No programming required, we just need the designs!
A sample of what the client is looking for:
http://velmorano.it/
Pages to include:
• Home – A nice slider design to showcase selected photos
• Main Category Template
• Sub Category Template
• About us
• Contact us
Example of their Main Categories and their Sub Categories:
Collections - Granite
- Marble
- Sculpture
Projects - Private
- Public
- Commercial
- Overseas
Installation - Vanity tops
- Hall areas
- Toilets
The Main Category is to show a sample and link the user to the respective Sub Categories. The Sub Categories are to showcase all the photos they have from the category. Please leave a little space to add some text or caption for the photo.
Designs need to be mobile responsive!
I've attached their logo and some sample photos to use for mock ups. Let me know if you have any questions!

```html
<!DOCTYPE html>
<html lang="en">
<head>
<meta charset="utf-8">
<title>Slate Haven – Installations</title>
<link href="https://fonts.googleapis.com/css2?family=Lato:wght@400;700;900&family=Oswald:wght@400;500&display=swap" rel="stylesheet">
<style>
:root{
  --page:#e6e6e6;
  --white:#ffffff;
  --ink:#2a2a2a;
  --text:#555555;
  --muted:#8a8a8a;
  --rule:#d6d6d6;
  --accent:#d01f1f;
  --soft:#f1f1f1;
  --footer:#2f2f2f;
  --footer-line:#4a4a4a;
  --footer-text:#e4e4e4;
  --icon:#1f1f1f;
}
*{margin:0;padding:0;box-sizing:border-box}
html,body{width:785px;height:1200px;overflow:hidden}
body{background:var(--page);font-family:"Lato",sans-serif;color:var(--text)}
.screen{
  position:absolute;left:214px;top:13px;width:254px;height:838px;
  background:var(--white);transform:scale(1.4);transform-origin:top left;
  overflow:hidden;box-shadow:0 0 3px rgba(0,0,0,.15);
}
.site-header{height:67px;display:flex;align-items:center;justify-content:center}
.brand{display:flex;align-items:center;gap:6px;font-weight:900;font-size:14px;color:var(--accent);letter-spacing:.5px}
.brand-mark{width:10px;height:10px;background:var(--accent)}
.nav-bar{height:25px;background:linear-gradient(#f4f4f4,#d9d9d9);position:relative;border-top:1px solid #cfcfcf}
.nav-btn{position:absolute;top:2px;width:22px;height:20px;background:var(--icon);border-radius:2px;display:flex;align-items:center;justify-content:center}
.nav-btn.menu{left:27px}
.nav-btn.phone{left:177px}
.nav-btn.mail{left:202px}
.slider{height:141px;position:relative;background:linear-gradient(180deg,#6e6e6e 0%,#bdbdbd 45%,#3b3b3b 100%)}
.slider-photo{position:absolute;inset:0}
.slide-caption{position:absolute;left:28px;top:52px;background:rgba(60,60,60,.6);color:var(--white);font-family:"Oswald",sans-serif;font-size:12px;padding:2px 6px;white-space:nowrap}
.slider-dots{position:absolute;left:108px;top:130px;display:flex;gap:3px}
.slider-dots span{width:6px;height:6px;border-radius:50%;background:var(--white)}
.slider-dots span.active{background:var(--accent)}
.content{padding:9px 28px 0 27px}
.section-title{font-weight:900;font-size:11px;color:var(--ink);letter-spacing:.2px}
.title-rule{height:2px;margin:5px 0 8px;background:linear-gradient(90deg,var(--ink) 0 84px,var(--rule) 84px)}
.content p{font-size:6.4px;line-height:9.7px;text-align:justify;margin-bottom:13px}
.feature-photo{margin-top:-1px;border:1px solid var(--rule);padding:2px;height:130px}
.feature-photo div{height:100%;background:linear-gradient(135deg,#b08a3e,#e6dcc8 55%,#8b6a33)}
.latest{margin-top:12px;background:var(--soft);height:108px;border-top:1px solid #e2e2e2;padding:10px 28px 0 28px}
.latest-title{font-family:"Oswald",sans-serif;font-size:9px;color:var(--accent)}
.latest-rule{width:70px;height:1px;background:var(--rule);margin:3px 0 6px}
.project{display:flex;gap:5px;margin-bottom:8px}
.project-thumb{width:27px;height:27px;flex:none;background:linear-gradient(135deg,#cfcfcf,#9a9a9a)}
.project-thumb.dark{background:linear-gradient(135deg,#7a7a7a,#3a3a3a)}
.project h4{font-size:7px;font-weight:700;color:var(--ink)}
.project p{font-size:6.3px;line-height:8.5px;color:var(--muted)}
.site-footer{background:var(--footer);height:117px;display:flex;padding:14px 0 0 27px;color:var(--footer-text)}
.footer-col h5{font-family:"Oswald",sans-serif;font-weight:400;font-size:9px;color:var(--footer-text)}
.footer-rule{width:48px;height:1px;background:var(--footer-line);margin:5px 0 8px}
.nav-list{list-style:none;font-size:6.4px;line-height:11px}
.nav-list li::before{content:"›";margin-right:4px}
.col-nav{width:78px;border-right:1px solid #3a3a3a;height:90px}
.col-contact{padding-left:20px}
.contact-row{display:flex;gap:6px;font-size:6.3px;line-height:8.5px;margin-bottom:8px;align-items:flex-start}
.contact-row b{font-weight:700}
.contact-row.phone{font-size:7.5px;font-weight:700;align-items:center}
.footer-bottom{background:var(--footer);border-top:1px solid var(--footer-line);height:53px;padding:6px 0 0 30px}
.social{display:flex;gap:4px}
.social span{width:20px;height:20px;border-radius:3px;background:#5a5a5a}
.copyright{font-size:6.2px;color:var(--footer-text);margin-top:9px}
</style>
</head>
<body>
<div class="screen">
  <header class="site-header">
    <div class="brand"><span class="brand-mark"></span>SLATE HAVEN</div>
  </header>
  <nav class="nav-bar">
    <span class="nav-btn menu"><svg width="13" height="10"><g stroke="#fff" stroke-width="1.6"><line x1="0" y1="1" x2="13" y2="1"/><line x1="0" y1="5" x2="13" y2="5"/><line x1="0" y1="9" x2="13" y2="9"/></g></svg></span>
    <span class="nav-btn phone"><svg width="10" height="10" viewBox="0 0 10 10"><path d="M2 0.5l2 2-1 1.3c.6 1.3 1.6 2.3 2.9 2.9l1.3-1 2 2-1.3 1.8C4 9 1 6 .3 1.8z" fill="#fff"/></svg></span>
    <span class="nav-btn mail"><svg width="13" height="9" viewBox="0 0 13 9"><rect x=".5" y=".5" width="12" height="8" fill="none" stroke="#fff"/><path d="M.5 .5l6 4.5 6-4.5" fill="none" stroke="#fff"/></svg></span>
  </nav>
  <section class="slider">
    <div class="slider-photo" role="img" aria-label="Hotel lobby interior with patterned stone floor and seating"></div>
    <div class="slide-caption">Lorem ipsum dolor sit amet adipiscing</div>
    <div class="slider-dots"><span class="active"></span><span></span><span></span><span></span></div>
  </section>
  <main class="content">
    <h2 class="section-title">INSTALLATIONS</h2>
    <div class="title-rule"></div>
    <p>Lorem ipsum dolor sit amet, consectetuer adipiscing elit, sed diam nonummy nibh euismod tincidunt ut laoreet dolore magna aliquam erat volutpat. Ut wisi enim ad minim veniam, quis nostrud exerci tation ullamcorper suscipit lobortis nisl ut aliquip ex ea commodo consequat. Duis autem vel eum iriure dolor in hendrerit in vulputate velit esse molestie consequat, vel illum dolore eu feugiat nulla facilisis at vero eros et accumsan</p>
    <p>et iusto odio dignissim qui blandit praesent luptatum zzril delenit augue duis dolore te feugait nulla facilisi. Lorem ipsum dolor sit amet, consectetuer adipiscing elit, sed diam nonummy nibh euismod tincidunt ut laoreet dolore magna aliquam erat volutpat. Ut wisi enim ad minim veniam, quis nostrud exerci tation ullamcorper suscipit lobortis nisl.</p>
    <div class="feature-photo"><div role="img" aria-label="Installer fitting a tiled kitchen backsplash"></div></div>
  </main>
  <section class="latest">
    <h3 class="latest-title">Latest Projects</h3>
    <div class="latest-rule"></div>
    <div class="project"><div class="project-thumb" role="img" aria-label="Light mosaic tile project"></div><div><h4>Lorem ipsum dolor</h4><p>Lorem ipsum dolor sit amet<br>adipiscing</p></div></div>
    <div class="project"><div class="project-thumb dark" role="img" aria-label="Interior project view"></div><div><h4>Lorem ipsum dolor</h4><p>Lorem ipsum dolor sit amet<br>adipiscing</p></div></div>
  </section>
  <footer class="site-footer">
    <div class="footer-col col-nav">
      <h5>Navigation</h5>
      <div class="footer-rule"></div>
      <ul class="nav-list"><li>Home</li><li>Collections</li><li>Projects</li><li>Installations</li><li>About Us</li><li>Contact Us</li></ul>
    </div>
    <div class="footer-col col-contact">
      <h5>Contact Us</h5>
      <div class="footer-rule"></div>
      <div class="contact-row"><svg width="7" height="9" viewBox="0 0 7 9"><path d="M3.5 0A3.3 3.3 0 0 0 .2 3.3C.2 5.5 3.5 9 3.5 9s3.3-3.5 3.3-5.7A3.3 3.3 0 0 0 3.5 0zm0 4.5a1.2 1.2 0 1 1 0-2.4 1.2 1.2 0 0 1 0 2.4z" fill="#e4e4e4"/></svg><span><b>Lorem ipsum dolor sit amet</b><br>consectetuer adimpisciged<br>diamr nonummy nibh</span></div>
      <div class="contact-row phone"><svg width="7" height="7" viewBox="0 0 10 10"><path d="M2 0.5l2 2-1 1.3c.6 1.3 1.6 2.3 2.9 2.9l1.3-1 2 2-1.3 1.8C4 9 1 6 .3 1.8z" fill="#e4e4e4"/></svg>123 456 7890</div>
      <div class="contact-row"><svg width="8" height="6" viewBox="0 0 13 9"><rect x=".5" y=".5" width="12" height="8" fill="#e4e4e4"/><path d="M.5 .5l6 4.5 6-4.5" fill="none" stroke="#2f2f2f"/></svg>info@slatehavenmktg.com</div>
    </div>
  </footer>
  <div class="footer-bottom">
    <div class="social"><span aria-label="Social link"></span><span aria-label="Video channel link"></span><span aria-label="Social link"></span><span aria-label="Professional network link"></span></div>
    <p class="copyright">© 2014 SlateHavenMarketing. All Right Reserved</p>
  </div>
</div>
</body>
</html>
```